Real Estate Sign 2

Our company is called Harwick Tolland Realty. We are a real estate development company. We need a sign that we are going to hang outside of our projects that says: Another project brought to you by Harwick Tolland Realty... For Sale....(213) 555-0847. At the very bottom is needs to say CaBRE# 04736291" We want the Harwick Tolland Realty to be sophisticated, fresh, simple. We do not have a logo so maybe one can be incorporated into the sign. Sign will be about 30"x24"

Industry/Entity Type

Real Estate

```html
<!DOCTYPE html>
<html lang="en">
<head>
<meta charset="utf-8">
<title>Harwick Tolland Realty — For Sale Sign</title>
<link rel="stylesheet" href="https://fonts.googleapis.com/css2?family=Bodoni+Moda:wght@700&family=Open+Sans:wght@400;600&display=swap">
<style>
  :root {
    --sign-red: #c00d1a;
    --sign-white: #ffffff;
  }
  html, body {
    margin: 0;
    padding: 0;
    width: 1200px;
    height: 960px;
    overflow: hidden;
    background: var(--sign-white);
  }
  .sign {
    display: block;
    width: 1200px;
    height: 960px;
  }
  .roof-band, .footer-band { fill: var(--sign-red); }
  .tagline {
    font-family: "Open Sans", sans-serif;
    font-weight: 400;
    font-size: 50px;
    fill: var(--sign-red);
  }
  .brand-name, .brand-type, .license {
    font-family: "Bodoni Moda", serif;
    font-weight: 700;
    fill: var(--sign-white);
  }
  .brand-name { font-size: 104px; }
  .brand-type { font-size: 82px; }
  .license { font-size: 40px; }
  .status, .phone {
    font-family: "Open Sans", sans-serif;
    font-weight: 600;
    fill: var(--sign-red);
  }
  .status { font-size: 166px; }
  .phone { font-size: 136px; }
</style>
</head>
<body>
<svg class="sign" viewBox="0 0 1200 960" xmlns="http://www.w3.org/2000/svg" role="img" aria-label="Harwick Tolland Realty for sale sign">
  <rect width="1200" height="960" fill="#ffffff"/>

  <text class="tagline" x="600" y="80" text-anchor="middle" textLength="1110" lengthAdjust="spacing">ANOTHER PROJECT BROUGHT TO YOU BY</text>

  <polygon class="roof-band" points="0,108 1200,108 1200,525 600,382 0,525"/>

  <text class="brand-name" x="600" y="240" text-anchor="middle" textLength="1110" lengthAdjust="spacingAndGlyphs">HARWICK TOLLAND</text>
  <text class="brand-type" x="600" y="329" text-anchor="middle" textLength="345" lengthAdjust="spacingAndGlyphs">REALTY</text>

  <text class="status" x="598" y="655" text-anchor="middle" textLength="880" lengthAdjust="spacingAndGlyphs">FOR SALE</text>
  <text class="phone" x="598" y="770" text-anchor="middle" textLength="880" lengthAdjust="spacingAndGlyphs">(213) 555-0847</text>

  <rect class="footer-band" x="0" y="822" width="1200" height="138"/>
  <text class="license" x="604" y="918" text-anchor="middle" textLength="352" lengthAdjust="spacingAndGlyphs">CaBRE# 04736291</text>
</svg>
</body>
</html>
```